Creating a Label for the Wine "Marvessa"

Marvessa
As you know Marvessa is an imagined place or state of things in which everything is perfect. This wine reflects that. It is a high value wine and it is perfect. The dimensions shoulb be between 9c x 11,5 cm and 12cm x 8 cm

```html
<!DOCTYPE html>
<html lang="en">
<head>
<meta charset="UTF-8">
<title>Marvessa – Sweet Red Wine Label</title>
<link rel="stylesheet" href="https://fonts.googleapis.com/css2?family=Great+Vibes&family=Oswald:wght@600&family=Fjalla+One&family=Montserrat:wght@700&display=swap">
<style>
  :root {
    --paper: #ffffff;
    --label: #4a1414;
    --band: #5c0f12;
    --scene-light: #f0222c;
    --scene-mid: #c8151e;
    --script: #e6d84a;
    --rule: #8f7487;
    --copy: #cfaec3;
    --name: #e8b4c6;
    --white: #ffffff;
    --frame: #5e2323;
  }
  html, body {
    margin: 0;
    width: 1000px;
    height: 1200px;
    overflow: hidden;
    background: var(--paper);
  }
  .label {
    position: absolute;
    left: 77px;
    top: 37px;
    width: 846px;
    height: 1128px;
    background: var(--label);
    overflow: hidden;
  }
  .label-frame {
    position: absolute;
    inset: 8px;
    border: 4px double var(--frame);
    pointer-events: none;
  }
  .title-rules {
    position: absolute;
    left: 258px;
    top: 28px;
    width: 505px;
    height: 170px;
  }
  .fine-wine {
    position: absolute;
    left: 258px;
    top: 52px;
    width: 505px;
    margin: 0;
    text-align: center;
    font-family: "Great Vibes", cursive;
    font-weight: 400;
    font-size: 96px;
    line-height: 1;
    word-spacing: 22px;
    color: var(--script);
  }
  .type-band {
    position: absolute;
    left: 0;
    top: 218px;
    width: 846px;
    height: 535px;
    background: var(--band);
  }
  .wine-type {
    position: absolute;
    left: 258px;
    top: 220px;
    width: 505px;
    margin: 0;
    text-align: center;
    font-family: "Oswald", sans-serif;
    font-weight: 600;
    font-size: 25px;
    letter-spacing: 2px;
    color: var(--copy);
  }
  .vineyard-scene {
    position: absolute;
    left: 0;
    top: 262px;
    width: 846px;
    height: 491px;
    background:
      linear-gradient(180deg, var(--band) 0%, var(--band) 22%, var(--scene-light) 30%, var(--scene-mid) 55%, var(--scene-light) 72%, var(--scene-mid) 100%);
    opacity: 0.9;
  }
  .name-column {
    position: absolute;
    left: 45px;
    top: 30px;
    width: 150px;
    height: 1070px;
    margin: 0;
    display: flex;
    flex-direction: column;
    justify-content: space-between;
    align-items: center;
    z-index: 2;
    font-family: "Fjalla One", sans-serif;
    font-weight: 400;
    font-size: 140px;
    line-height: 128px;
    color: var(--name);
  }
  .name-letter {
    display: block;
    height: 128px;
  }
  .story {
    position: absolute;
    left: 230px;
    top: 780px;
    width: 560px;
    margin: 0;
    text-align: center;
    font-family: "Fjalla One", sans-serif;
    font-size: 26px;
    line-height: 37px;
    color: var(--copy);
  }
  .origin {
    position: absolute;
    left: 230px;
    top: 955px;
    width: 560px;
    margin: 0;
    text-align: center;
    font-family: "Fjalla One", sans-serif;
    font-size: 26px;
    color: var(--copy);
  }
  .abv, .volume {
    position: absolute;
    margin: 0;
    font-family: "Montserrat", sans-serif;
    font-weight: 700;
    color: var(--white);
    line-height: 1;
  }
  .abv { left: 222px; top: 1056px; font-size: 42px; }
  .volume { left: 676px; top: 1040px; font-size: 56px; }
  .unit { font-size: 14px; margin-left: 3px; }
</style>
</head>
<body>
  <main class="label">
    <div class="label-frame"></div>

    <svg class="title-rules" viewBox="0 0 505 170" aria-hidden="true">
      <line x1="0" y1="10" x2="235" y2="10" stroke="var(--rule)" stroke-width="1.5"/>
      <line x1="270" y1="10" x2="505" y2="10" stroke="var(--rule)" stroke-width="1.5"/>
      <polygon points="245,12 252,3 259,12" fill="var(--rule)"/>
      <line x1="0" y1="162" x2="235" y2="162" stroke="var(--rule)" stroke-width="1.5"/>
      <line x1="270" y1="162" x2="505" y2="162" stroke="var(--rule)" stroke-width="1.5"/>
      <polygon points="245,160 252,169 259,160" fill="var(--rule)"/>
    </svg>
    <h2 class="fine-wine">Fine Wine</h2>

    <div class="type-band"></div>
    <div class="vineyard-scene" role="img" aria-label="Red-toned landscape of a coastal vineyard with grasses and a distant house"></div>
    <p class="wine-type">SWEET RED WINE</p>

    <h1 class="name-column" aria-label="Marvessa">
      <span class="name-letter">M</span>
      <span class="name-letter">A</span>
      <span class="name-letter">R</span>
      <span class="name-letter">V</span>
      <span class="name-letter">E</span>
      <span class="name-letter">S</span>
      <span class="name-letter">S</span>
      <span class="name-letter">A</span>
    </h1>

    <p class="story">
      Blended from the XXX vineyards with<br>
      a long standing tradition of fine wines since 1947.<br>
      Our wines are smooth and full in body.<br>
      Caution: May contain Sulphites.
    </p>
    <p class="origin">Product of Italy</p>

    <p class="abv">11%<span class="unit">VOL.</span></p>
    <p class="volume">750<span class="unit">ML</span></p>
  </main>
</body>
</html>
```